Soho based IT support firm flyer.

We need a flyer to boost our business. We're a tech support firm based in Soho, London and provide helpdesk and call out support to SMEs in and around London.
They'll be two flyers with the same design. One is location specific and has the copy:
-
1 Month Free IT Support!
Based in Soho, we provide expert tech support for both desktops and laptops.
We have monthly as well as pay-as-you-go plans to fit your business.
Call us now and we'll show you how we can save you up to 50% on your IT spend.
-None location based is-
1 Month Free IT Support!
We provide expert, professional tech support for both desktops and laptops.
• Dedicated full time helpdesk
• Same day onsite visits
• Proactive support with monitoring
• 98% satisfaction score*
*taken from satisfaction survey sent out on closure of every case for Oct 2011 to Oct 2012
-
The location one needs to include a map with our location marked as postcode W9K 4TP.
I'm fine with royalty photos being used within a reasonable price. Please use PixQuarry.
Our site shows our brand best. Please keep as close to this as possible.
http://brisk-byte.example
Thanks for looking.

```html
<!DOCTYPE html>
<html lang="en">
<head>
<meta charset="utf-8">
<title>BriskByte – Friendly &amp; Reliable Tech Support</title>
<link rel="stylesheet" href="https://fonts.googleapis.com/css2?family=Roboto+Condensed:wght@400;700;800&display=swap">
<style>
  :root {
    --lime: #9ccb2c;
    --lime-light: #c3e04a;
    --lime-dark: #5e9a1a;
    --orange: #f47b20;
    --orange-light: #f9a440;
    --ink: #1f1f1f;
    --heading-grey: #6f6f6f;
    --bar-dark: #1a1a1a;
    --white: #ffffff;
  }
  * { box-sizing: border-box; margin: 0; padding: 0; }
  html, body { width: 849px; height: 1200px; overflow: hidden; background: var(--white); }
  .flyer {
    position: relative; width: 849px; height: 1200px; overflow: hidden;
    font-family: "Roboto Condensed", "Arial Narrow", sans-serif; background: var(--white);
  }
  .backdrop { position: absolute; inset: 0; }
  .phone-bar {
    position: absolute; left: 0; top: 0; width: 380px; height: 100px;
    background: var(--bar-dark); border-radius: 0 0 40px 0;
    display: flex; align-items: center; gap: 16px; padding-left: 26px;
    color: var(--white); font-weight: 700; font-size: 44px; letter-spacing: 0.5px;
  }
  .phone-bar svg { width: 38px; height: 38px; flex: none; }
  .offer-badge {
    position: absolute; left: 62px; top: 168px; width: 212px; height: 212px; border-radius: 50%;
    background: radial-gradient(circle at 40% 35%, var(--orange-light), var(--orange) 70%);
    border: 9px solid var(--white); box-shadow: 0 4px 14px rgba(0,0,0,.25);
    display: flex; flex-direction: column; align-items: center; justify-content: center;
    color: var(--white); font-weight: 700; text-align: center; line-height: 1;
  }
  .offer-badge .offer-inner { transform: rotate(-14deg); }
  .offer-badge .offer-free { font-size: 62px; }
  .offer-badge .offer-detail { font-size: 30px; margin-top: 4px; }
  .headline {
    position: absolute; left: 60px; top: 456px; color: var(--heading-grey);
    font-weight: 700; font-size: 56px; line-height: 1.14;
  }
  .benefits {
    position: absolute; left: 40px; top: 662px; width: 790px;
    display: grid; grid-template-columns: 420px 340px; column-gap: 20px;
  }
  .benefits ul { list-style: none; }
  .benefits li {
    position: relative; padding-left: 44px; margin-bottom: 18px;
    color: var(--ink); font-weight: 800; font-size: 28px; line-height: 1.06;
  }
  .benefits li::before {
    content: ""; position: absolute; left: 0; top: 3px; width: 20px; height: 20px;
    border: 5px solid var(--white); border-radius: 50%;
  }
  .footnote {
    position: absolute; left: 34px; top: 1002px; color: var(--ink);
    font-size: 20px;
  }
  .contact {
    position: absolute; left: 32px; top: 1098px; list-style: none;
    color: var(--white); font-size: 26px; line-height: 1.7;
  }
  .contact li { display: flex; align-items: center; gap: 14px; }
  .contact li::before { content: ""; width: 13px; height: 13px; background: var(--white); }
  .brand-name {
    position: absolute; left: 420px; top: 1092px; color: var(--lime);
    font-weight: 700; font-size: 70px; letter-spacing: 1px; line-height: 1;
  }
</style>
</head>
<body>
<main class="flyer">
  <svg class="backdrop" width="849" height="1200" viewBox="0 0 849 1200" aria-hidden="true">
    <defs>
      <linearGradient id="photoTone" x1="0" y1="0" x2="1" y2="1">
        <stop offset="0" stop-color="#e9eef2"/>
        <stop offset="0.45" stop-color="#d8c2b0"/>
        <stop offset="1" stop-color="#9fb6cf"/>
      </linearGradient>
      <linearGradient id="bandTone" x1="0" y1="0" x2="0" y2="1">
        <stop offset="0" stop-color="#b5d93a"/>
        <stop offset="1" stop-color="#8fc12a"/>
      </linearGradient>
      <linearGradient id="swooshTone" x1="0" y1="0" x2="1" y2="0">
        <stop offset="0" stop-color="#c7e24c"/>
        <stop offset="1" stop-color="#8cc22a"/>
      </linearGradient>
    </defs>
    <path d="M0 330 C 250 450, 560 430, 849 260 L 849 330 C 600 470, 260 500, 0 420 Z" fill="url(#swooshTone)"/>
    <path d="M0 420 C 260 500, 600 470, 849 330 L 849 345 C 600 485, 260 515, 0 432 Z" fill="var(--lime-dark)"/>
    <rect x="0" y="627" width="849" height="363" fill="url(#bandTone)"/>
    <path d="M0 1070 C 300 1064, 560 1050, 849 1030 L 849 1044 C 560 1066, 300 1080, 0 1084 Z" fill="var(--lime)"/>
    <path d="M0 1084 L 360 1084 C 392 1084, 400 1200, 430 1200 L 0 1200 Z" fill="var(--orange)"/>
  </svg>

  <svg class="backdrop" width="849" height="1200" viewBox="0 0 849 1200" role="img"
       aria-label="Photo: three smiling office colleagues gathered around a laptop">
    <path d="M262 0 L 849 0 L 849 262 C 640 395, 420 410, 300 360 C 270 250, 262 120, 262 0 Z" fill="url(#photoTone)"/>
  </svg>

  <div class="phone-bar">
    <svg viewBox="0 0 24 24" aria-hidden="true"><path fill="#ffffff" d="M6.6 10.8a15.1 15.1 0 0 0 6.6 6.6l2.2-2.2a1 1 0 0 1 1-.25 11.4 11.4 0 0 0 3.6.57 1 1 0 0 1 1 1V20a1 1 0 0 1-1 1A17 17 0 0 1 3 4a1 1 0 0 1 1-1h3.5a1 1 0 0 1 1 1c0 1.25.2 2.45.57 3.6a1 1 0 0 1-.25 1z"/></svg>
    <span>0203 555 0147</span>
  </div>

  <div class="offer-badge">
    <div class="offer-inner">
      <div class="offer-free">FREE</div>
      <div class="offer-detail">One Month<br>IT Support!</div>
    </div>
  </div>

  <h1 class="headline">Friendly &amp;<br>Reliable Tech Support</h1>

  <section class="benefits">
    <ul>
      <li>We provide expert,<br>professional tech support<br>for both desktops and laptops.</li>
      <li>We have monthly as well as<br>pay-as-you-go plans to fit<br>your business.</li>
      <li>Call us now and we’ll show<br>you how we can save you<br>up to 50% on your IT spend.</li>
    </ul>
    <ul>
      <li>Dedicated full time<br>helpdesk</li>
      <li>Same day onsite visits</li>
      <li>Proactive support<br>with monitoring</li>
      <li>98% satisfaction score*</li>
    </ul>
  </section>

  <p class="footnote">*taken from satisfaction survey sent out on closure of every case for Oct 2011 to Oct 2012</p>

  <ul class="contact">
    <li>info@brisk-byte.example</li>
    <li>www.brisk-byte.example</li>
  </ul>

  <div class="brand-name">BriskByte</div>
</main>
</body>
</html>
```